Lanternfield Ministries Project Harvestline

I have a pop up display for inside tradeshows I would like for you to design. Here are the dimensions

pop up stand: 33(left side)+300+33cm(right side)

prodium: 1.04*2.2m

X stand: 60*160cm
I want to use the grayscale color wheel.
I want the backwall, xframes, and prodium to flow cohesively. I give you creative control on this project. Afterwards we will collaborate on the details. I want light gray from top gradually fading down to black which should be on the bottom.

Target Market(s)

Men and women from ages 16-59 yrs of age

Industry/Entity Type

Religious/ministry

Font styles to use
Serif

Colors

Designer to choose only greyscale colors for use in the design.

Requirements
Should not have
• N/a

```html
<!DOCTYPE html>
<html lang="en">
<head>
<meta charset="utf-8">
<title>Lanternfield Ministries – Tradeshow Display Artwork</title>
<link href="https://fonts.googleapis.com/css2?family=Archivo+Black&family=Cormorant+Garamond:wght@600&family=Outfit:wght@300;400&display=swap" rel="stylesheet">
<style>
  :root {
    --stage: #a19fa0;
    --label: #ffffff;
    --ink: #0c0c0c;
    --paper: #ffffff;
    --mist: #ececec;
    --mid: #9c9c9c;
    --night: #050505;
    --ghost: rgba(0,0,0,0.32);
    --ghost-soft: rgba(0,0,0,0.16);
  }
  * { margin: 0; padding: 0; box-sizing: border-box; }
  html, body { width: 1200px; height: 1135px; overflow: hidden; }
  body { background: var(--stage); position: relative; font-family: "Outfit", sans-serif; }

  .piece-title {
    position: absolute; top: 70px; transform: translateX(-50%);
    color: var(--label); font-family: "Outfit", sans-serif; font-weight: 400;
    font-size: 27px; white-space: nowrap; letter-spacing: 0.2px;
  }
  .panel-label {
    position: absolute; top: 114px; transform: translateX(-50%);
    color: var(--label); font-family: "Outfit", sans-serif; font-weight: 300;
    font-size: 17px; letter-spacing: 0.5px;
  }

  .panel {
    position: absolute; top: 145px; height: 360px; overflow: hidden;
    background: linear-gradient(to bottom,
      var(--paper) 0%, var(--mist) 40%, var(--mid) 58%, #3a3a3a 75%, var(--night) 100%);
  }
  .x-stand { left: 76px; width: 144px; }
  .popup-left { left: 265px; width: 72px; }
  .popup-center { left: 345px; width: 362px; }
  .popup-right { left: 713px; width: 72px; }
  .podium { left: 830px; width: 295px; }

  .lockup { position: absolute; display: flex; flex-direction: column; align-items: center; transform: translateX(-50%); }
  .lockup-mark { background: var(--ink); border-radius: 4px; }
  .lockup-name {
    font-family: "Cormorant Garamond", serif; font-weight: 600; color: var(--ink);
    white-space: nowrap; line-height: 1.1;
  }
  .lockup-tagline {
    font-family: "Outfit", sans-serif; font-weight: 400; color: var(--ink);
    white-space: nowrap; letter-spacing: 0.28em; align-self: flex-end;
  }

  .x-stand .lockup { left: 72px; top: 32px; }
  .x-stand .lockup-mark { width: 34px; height: 24px; }
  .x-stand .lockup-name { font-size: 12.5px; margin-top: 4px; }
  .x-stand .lockup-tagline { font-size: 3.6px; }

  .popup-center .lockup { left: 181px; top: 46px; }
  .popup-center .lockup-mark { width: 62px; height: 45px; }
  .popup-center .lockup-name { font-size: 22px; margin-top: 8px; }
  .popup-center .lockup-tagline { font-size: 5.4px; }

  .podium .lockup { left: 148px; top: 58px; }
  .podium .lockup-mark { width: 64px; height: 46px; }
  .podium .lockup-name { font-size: 22.5px; margin-top: 8px; }
  .podium .lockup-tagline { font-size: 5.4px; }

  .ghost-name {
    position: absolute; font-family: "Cormorant Garamond", serif; font-weight: 600;
    color: var(--ghost); white-space: nowrap; line-height: 1;
  }
  .ghost-tagline {
    font-family: "Outfit", sans-serif; font-weight: 400; letter-spacing: 0.28em;
    color: var(--ghost-soft); display: block; text-align: right;
  }
  .x-stand .ghost-name {
    font-size: 22px; left: 50%; top: 240px;
    transform: translate(-50%, -50%) rotate(-90deg);
  }
  .x-stand .ghost-tagline { font-size: 4.5px; margin-top: 2px; }
  .podium .ghost-name { font-size: 30px; left: 50%; top: 232px; transform: translateX(-50%); }
  .podium .ghost-tagline { font-size: 5.5px; margin-top: 3px; }

  .slogan-band { position: absolute; top: 240px; width: 520px; height: 80px; }
  .popup-left .slogan-band { left: 0; }
  .popup-center .slogan-band { left: -80px; }
  .popup-right .slogan-band { left: -448px; }
  .slogan-band text { font-family: "Archivo Black", sans-serif; }
  .slogan-line-top { fill: rgba(0,0,0,0.28); }
  .slogan-line-bottom { fill: rgba(0,0,0,0.55); }
</style>
</head>
<body>
  <h2 class="piece-title" style="left:148px">X-Stand</h2>
  <h2 class="piece-title" style="left:526px">Pop-Up Banner</h2>
  <h2 class="piece-title" style="left:978px">Podium</h2>
  <span class="panel-label" style="left:301px">Left</span>
  <span class="panel-label" style="left:526px">Center</span>
  <span class="panel-label" style="left:748px">Right</span>

  <section class="panel x-stand">
    <div class="lockup">
      <div class="lockup-mark"></div>
      <div class="lockup-name">Lanternfield Ministries</div>
      <div class="lockup-tagline">A GIFT GIVEN IS A STEP UP</div>
    </div>
    <div class="ghost-name">Lanternfield Ministries<span class="ghost-tagline">A GIFT GIVEN IS A STEP UP</span></div>
  </section>

  <section class="panel popup-left">
    <svg class="slogan-band" viewBox="0 0 520 80" aria-hidden="true">
      <text class="slogan-line-top" x="0" y="31" font-size="36" textLength="520" lengthAdjust="spacingAndGlyphs">A GIFT GIVEN IS A</text>
      <text class="slogan-line-bottom" x="51" y="71" font-size="48" textLength="418" lengthAdjust="spacingAndGlyphs">STEP UP</text>
    </svg>
  </section>

  <section class="panel popup-center">
    <div class="lockup">
      <div class="lockup-mark"></div>
      <div class="lockup-name">Lanternfield Ministries</div>
      <div class="lockup-tagline">A GIFT GIVEN IS A STEP UP</div>
    </div>
    <svg class="slogan-band" viewBox="0 0 520 80" aria-hidden="true">
      <text class="slogan-line-top" x="0" y="31" font-size="36" textLength="520" lengthAdjust="spacingAndGlyphs">A GIFT GIVEN IS A</text>
      <text class="slogan-line-bottom" x="51" y="71" font-size="48" textLength="418" lengthAdjust="spacingAndGlyphs">STEP UP</text>
    </svg>
  </section>

  <section class="panel popup-right">
    <svg class="slogan-band" viewBox="0 0 520 80" aria-hidden="true">
      <text class="slogan-line-top" x="0" y="31" font-size="36" textLength="520" lengthAdjust="spacingAndGlyphs">A GIFT GIVEN IS A</text>
      <text class="slogan-line-bottom" x="51" y="71" font-size="48" textLength="418" lengthAdjust="spacingAndGlyphs">STEP UP</text>
    </svg>
  </section>

  <section class="panel podium">
    <div class="lockup">
      <div class="lockup-mark"></div>
      <div class="lockup-name">Lanternfield Ministries</div>
      <div class="lockup-tagline">A GIFT GIVEN IS A STEP UP</div>
    </div>
    <div class="ghost-name">Lanternfield Ministries<span class="ghost-tagline">A GIFT GIVEN IS A STEP UP</span></div>
  </section>
</body>
</html>
```